Premium Skincare Packaging Design for Vale Hollow

Vale Hollow (https://valehollow-example.com) is a premium wellness brand from Canada specializing in beef tallow (for cooking) and now expanding into natural skincare. We are seeking packaging design concepts for two new 60 ml skincare products made with grass-fed beef tallow.
Our goal is to achieve a clean, minimalist yet luxurious look that reflects purity, quality and sophistication. The design should look premium enough for high-end skincare shelves while maintaining a natural, grounded feel.
You will be designing:
- Jar label (wrap-around design) for a 60 ml glass jar with black lid
- Round lid sticker (for the top of the black lid)
- Square outer box (for each jar)
- Both products are very similar, so the differentiation can be minimal.

Products to Design
1. All-Purpose Tallow Balm
Jar: Frosted glass, 60 ml with black lid
Purpose: Moisturizer for face, lips, hands, and body
Ingredients: Grass-fed beef tallow, beeswax, honey, vitamin E
Tone: Natural, pure, versatile, gentle
Tagline: “Crafted from nature’s simplest elements”
Preferred color palette:
Light / off-white background
Beige and honey accents
Black or dark brown typography
Mood: Minimalist apothecary meets warm, natural simplicity
2. Face Tallow Cream
Purpose: Face moisturizer with nourishing tallow and botanicals
Tone: Refined, elegant, modern, premium
Tagline: “The strength of tallow, refined for your face”
Preferred color palette:
Deep charcoal or black background
Gold or cream typography
Accent in subtle metallic tones (gold or bronze)
Mood: Modern luxury with understated confidence
Design Deliverables
For each product, submit:
1) Jar Label (Wrap-around)
- Include product name, logo, tagline, ingredients, and size (60 ml / 2 fl oz).
- Space for barcode and manufacturing details (leave placeholder).
2) Round Lid Sticker
- Centered logo and minimalist border or accent ring.
3) Outer Paper Box (Square)
- Matching color palette and typography.
- Clean layout featuring the Vale Hollow logo and tagline.
- Text to include: product name, tagline, ingredients and size.

Brand Guidelines
Logo: Use the existing Vale Hollow logo (we’ll upload it for reference).
Typography: Clean and elegant — sans-serif or classic serif fonts.
Tone: Pure, premium, and intentional — less is more.
Design cohesion: Both products must look like part of one collection.

```html
<!DOCTYPE html>
<html lang="en">
<head>
<meta charset="utf-8">
<title>Vale Hollow – All-Purpose Tallow Balm Label</title>
<link rel="stylesheet" href="https://fonts.googleapis.com/css2?family=Outfit:wght@500;600&family=Barlow:wght@500&family=Arimo:ital@0;1&display=swap">
<style>
  :root {
    --page: #ffffff;
    --label: #333233;
    --gold: #d2ad6c;
    --ink: #ffffff;
  }
  html, body {
    margin: 0;
    padding: 0;
    width: 874px;
    height: 1200px;
    overflow: hidden;
    background: var(--page);
  }
  .sheet {
    position: relative;
    width: 874px;
    height: 1200px;
  }
  .label {
    position: absolute;
    left: 74px;
    width: 725px;
    display: block;
  }
  .label--full { top: 245px; height: 469px; }
  .label--compact { top: 774px; height: 181px; }
  .label-base { fill: var(--label); }
  .gold-band { fill: var(--gold); }
  .brand-name {
    font-family: "Outfit", sans-serif;
    font-weight: 500;
    fill: var(--ink);
    letter-spacing: 0.08em;
  }
  .product-name {
    font-family: "Outfit", sans-serif;
    font-weight: 600;
    fill: var(--ink);
    letter-spacing: 0.02em;
  }
  .tagline, .size {
    font-family: "Barlow", sans-serif;
    font-weight: 500;
    fill: var(--ink);
    letter-spacing: 0.03em;
  }
  .info {
    font-family: "Arimo", sans-serif;
    fill: var(--ink);
  }
  .info-heading { font-style: italic; }
</style>
</head>
<body>
<main class="sheet">

  <svg class="label label--full" viewBox="0 0 725 469" aria-label="Wrap-around jar label">
    <rect class="label-base" width="725" height="469"/>
    <rect class="gold-band" y="30" width="725" height="9.5"/>
    <rect class="gold-band" y="430" width="725" height="9.5"/>

    <text class="brand-name" x="237" y="110" font-size="30" text-anchor="middle">VALE HOLLOW</text>

    <text class="product-name" x="237" y="224" font-size="44" text-anchor="middle">ALL-PURPOSE</text>
    <text class="product-name" x="237" y="275" font-size="44" text-anchor="middle">TALLOW BALM</text>

    <text class="tagline" x="237" y="326" font-size="15" text-anchor="middle">crafted from nature’s simplest elements</text>
    <text class="size" x="237" y="409" font-size="15" text-anchor="middle">60 ml</text>

    <text class="info" x="499" y="106" font-size="12.5">
      <tspan class="info-heading">Purpose:</tspan>
      <tspan x="499" dy="14.8">Moisturizer for face, lips,</tspan>
      <tspan x="499" dy="14.8">hands, and body</tspan>
    </text>
    <text class="info" x="493" y="176" font-size="12.5">
      <tspan class="info-heading">Ingredients</tspan><tspan>:</tspan>
      <tspan x="493" dy="14.8">Grass-fed beef tallow,</tspan>
      <tspan x="493" dy="14.8">beeswax, honey, vitamin E</tspan>
    </text>
  </svg>

  <svg class="label label--compact" viewBox="0 0 725 181" aria-label="Compact jar label">
    <rect class="label-base" width="725" height="181"/>
    <rect class="gold-band" y="165" width="725" height="4.5"/>

    <text class="brand-name" x="90" y="46" font-size="11" text-anchor="middle">VALE HOLLOW</text>

    <text class="product-name" x="90" y="94" font-size="17" text-anchor="middle">ALL-PURPOSE</text>
    <text class="product-name" x="90" y="114" font-size="17" text-anchor="middle">TALLOW BALM</text>

    <text class="tagline" x="90" y="133" font-size="6.3" text-anchor="middle">crafted from nature’s simplest elements</text>

    <text class="info" x="393" y="41" font-size="4.8">
      <tspan class="info-heading">Purpose:</tspan>
      <tspan x="393" dy="5.8">Moisturizer for face, lips,</tspan>
      <tspan x="393" dy="5.8">hands, and body</tspan>
    </text>
    <text class="info" x="390" y="68" font-size="4.8">
      <tspan class="info-heading">Ingredients:</tspan>
      <tspan x="390" dy="5.8">Grass-fed beef tallow,</tspan>
      <tspan x="390" dy="5.8">beeswax, honey, vitamin E</tspan>
    </text>

    <text class="size" x="477" y="144" font-size="6">60 ml</text>
  </svg>

</main>
</body>
</html>
```